Motion Nest Business Cards

Can all designers please apply the following info on their designs' back-side of the business card: (please see brief file upload ('Info for backside...' - for required info, colours & layout)

SPECIALISING IN INDIVIDUAL PILATES INSTRUCTION
MATWORK – including small apparatus
and STUDIO:
VIVANTE 3 GLIDER
LADDER BARREL
COUNTOUR BARREL
FLEXI DOME
VIM STOOL
KIM-O-LAN

Business Cards for Motion Nest - applying the Motion Nest logo design selected earlier.
Note the business card requires both a front and back side. Please refer to two uploaded ppt-files for type of info required to be displayed, and rough position of where info could be. Require innovative / fresh approach to business card design and use of colour by designers now. Please refer to and use logo as uploaded - also for potential business card colour application.

Dear Designers,

Please note the additional inclusion / upload of two draft ppt-files that try to show where I want what type of information, for both the front & back sides of the required business card, plus an attempt at showing the high-level concept / idea of business info position.

As my 'drafts' obviously lack colour and any ability towards innovative card design or approach – I now rely on your vastly superior graphic design abilities to produce a really great business card for my business…

Looking forward to your submissions!

Kind regards, Merika for: Motion Nest 

Hello all Designers,

Can all designers please apply the following info on their designs' back-side of the business card: (please see / refer to the Brief and specifically the file upload ('Info for backside...' - for required info, colours & layout) - for the backside of the business card).

Info content (without colour, layout etc.):

and STUDIO:

VIVANTE 3 GLIDER

LADDER BARREL

COUNTOUR BARREL

FLEXI DOME

VIM STOOL

KIM-O-LAN

Thank you to all designers that submitted for consideration!

With regards,

Motion Nest

```html
<!DOCTYPE html>
<html lang="en">
<head>
<meta charset="utf-8">
<title>Motion Nest – Business Card</title>
<link href="https://fonts.googleapis.com/css2?family=Montserrat:wght@400;700&family=Open+Sans:wght@300;700&family=Architects+Daughter&display=swap" rel="stylesheet">
<style>
  :root {
    --bg: #e9e6e1;
    --green: #8cc63f;
    --green-deep: #79b330;
    --green-dark: #2f5a1e;
    --orange: #ec8a1f;
    --logo-red: #d9481f;
    --white: #ffffff;
    --ink: #3d5a26;
    --card-radius: 16px;
  }
  * { box-sizing: border-box; margin: 0; padding: 0; }
  html, body { width: 1200px; height: 900px; overflow: hidden; }
  body { background: var(--bg); position: relative; font-family: "Open Sans", sans-serif; }

  .card {
    position: absolute;
    width: 560px; height: 320px;
    border-radius: var(--card-radius);
    overflow: hidden;
    box-shadow: 0 10px 28px rgba(0,0,0,.18);
  }

  /* ---------- Back side ---------- */
  .card-back {
    left: 70px; top: 90px;
    background: linear-gradient(135deg, var(--green) 0%, var(--green-deep) 100%);
    color: var(--white);
  }
  .card-back .edge-strip {
    position: absolute; left: 0; top: 0; bottom: 0; width: 34px;
    background: var(--orange);
  }
  .card-back .specialty {
    position: absolute; left: 62px; top: 34px; right: 30px;
    font-weight: 700; font-size: 15px; line-height: 1.35; letter-spacing: .2px;
    text-transform: uppercase;
  }
  .card-back .studio-list {
    position: absolute; left: 62px; top: 112px; width: 260px;
    list-style: none; text-align: center;
    font-weight: 300; font-size: 16px; line-height: 1.42; letter-spacing: .6px;
    text-transform: uppercase;
  }

  /* ---------- Front side ---------- */
  .card-front {
    left: 570px; top: 490px;
    background: var(--white);
  }
  .brand {
    position: absolute; left: 40px; top: 30px;
    display: flex; align-items: center; gap: 14px;
  }
  .brand-dot { width: 30px; height: 30px; border-radius: 50%; background: var(--green-dark); }
  .brand-name {
    font-family: "Montserrat", sans-serif; font-weight: 400; font-size: 38px;
    color: var(--logo-red); letter-spacing: .5px;
  }
  .band-orange {
    position: absolute; left: 0; right: 0; top: 96px; height: 78px;
    background: var(--orange);
  }
  .holder {
    position: absolute; left: 150px; top: 108px; color: var(--white);
  }
  .holder-name { font-family: "Montserrat", sans-serif; font-weight: 700; font-size: 19px; }
  .holder-title { font-size: 11px; margin-top: 3px; }
  .band-green {
    position: absolute; left: 0; right: 0; top: 174px; height: 84px;
    background: var(--green);
  }
  .address {
    position: absolute; left: 40px; top: 196px;
    display: flex; gap: 10px; color: var(--white);
    font-family: "Montserrat", sans-serif; font-weight: 700; font-size: 13px; line-height: 1.4;
  }
  .contacts {
    position: absolute; left: 330px; top: 184px; list-style: none;
    color: var(--white); font-size: 12.5px; line-height: 1.6;
  }
  .contacts li, .address { align-items: flex-start; }
  .contacts li { display: flex; align-items: center; gap: 9px; }
  .icon { width: 13px; height: 13px; flex: none; }
  .address .icon { margin-top: 2px; }
  .tagline {
    position: absolute; left: 0; right: 0; top: 272px; text-align: center;
    font-family: "Architects Daughter", cursive; font-size: 19px; letter-spacing: 2px;
    color: var(--ink);
  }
</style>
</head>
<body>

  <section class="card card-back" aria-label="Business card, back">
    <div class="edge-strip"></div>
    <p class="specialty">Specialising in individual Pilates instruction<br>Matwork (incl. small apparatus)</p>
    <ul class="studio-list">
      <li>Studio:</li>
      <li>Vivante 3 Glider</li>
      <li>Ladder Barrel</li>
      <li>Countour Barrel</li>
      <li>Flexi Dome</li>
      <li>Vim Stool</li>
      <li>Kim-o-lan</li>
    </ul>
  </section>

  <section class="card card-front" aria-label="Business card, front">
    <div class="brand">
      <span class="brand-dot"></span>
      <span class="brand-name">Motion Nest</span>
    </div>

    <div class="band-orange"></div>
    <div class="holder">
      <p class="holder-name">Merika Kowalczyk</p>
      <p class="holder-title">Diploma of Professional Pilates Instruction</p>
    </div>

    <div class="band-green"></div>
    <div class="address">
      <svg class="icon" viewBox="0 0 12 16"><path d="M6 0a6 6 0 0 0-6 6c0 4.5 6 10 6 10s6-5.5 6-10a6 6 0 0 0-6-6zm0 8.3A2.3 2.3 0 1 1 6 3.7a2.3 2.3 0 0 1 0 4.6z" fill="#d9481f"/></svg>
      <span>18 Harwood Lane<br>Lakefield WA 6099</span>
    </div>
    <ul class="contacts">
      <li><svg class="icon" viewBox="0 0 12 16"><rect x="1.5" y="0.5" width="9" height="15" rx="1.5" fill="none" stroke="#d9481f" stroke-width="1.4"/><circle cx="6" cy="13" r="1" fill="#d9481f"/></svg>041 555 0192</li>
      <li><svg class="icon" viewBox="0 0 16 12"><rect x="0.7" y="0.7" width="14.6" height="10.6" fill="#d9481f"/><path d="M1 1l7 6 7-6" fill="none" stroke="#fff" stroke-width="1.2"/></svg>info@motionnest.com</li>
      <li><svg class="icon" viewBox="0 0 16 14"><path d="M8 0L0 7h2v7h4V9h4v5h4V7h2z" fill="#d9481f"/></svg>www.motionnest.com.au</li>
    </ul>

    <p class="tagline">BALANCE &nbsp;-&nbsp; STRENGTH &nbsp;-&nbsp; FLEXIBILITY</p>
  </section>

</body>
</html>
```